Professional Music Editor Needs a Book Cover Design

I need a book cover design for a series of books which will include excerpts from symphonic pieces required for auditions in professional symphony orchestras. The books will contain text and a lot of music examples. The book will be published in a Pagro and Tomeo version, to be used mainly on an Zelt, but will be also available in print in A4 size. The cover may incorporate notation or/and violin images.

The text on the cover should include:

Author: Dariel Vomanek D.M.A.
Series: The Weekly Handful Ensemble Fragments for Viola
Title: Anselm Korvath, Lune Orvel Op. 20, measures 1-62

Thank you so much for the submitted projects so far! I have uploaded one more photo, which I think may be a good element to use. If you decide to incorporate it, please use just the violin from the photo, not the person. 

And one more thing: I would like the design to be modern, rather than traditional.

Thanks a lot for your work!

Target Market(s)

The target customers of this edition are college students who are going to use the book to prepare for auditions for professional orchestras.

Industry/Entity Type

It Professional

Colors
ffffff

```html
<!DOCTYPE html>
<html lang="en">
<head>
<meta charset="utf-8">
<title>The Weekly Handful Series – Ensemble Fragments for Viola</title>
<link rel="stylesheet" href="https://fonts.googleapis.com/css2?family=Cinzel:wght@400;600;700&display=swap">
<style>
  :root {
    --paper: #ffffff;
    --wine: #6e1a22;
    --rule: #b8484e;
    --ink: #141414;
    --outline: #3a3a3a;
    --forest: #1c4a1a;
    --wood-deep: #6a2410;
    --wood-mid: #a8481f;
    --wood-light: #c86a34;
    --sheet-light: #eeeceb;
    --sheet-grey: #d4d2d0;
  }
  * { margin: 0; padding: 0; box-sizing: border-box; }
  html, body { width: 848px; height: 1200px; overflow: hidden; background: var(--paper); }
  .cover {
    position: relative;
    width: 848px;
    height: 1200px;
    background: var(--paper);
    font-family: "Cinzel", serif;
    overflow: hidden;
  }
  .series-name {
    position: absolute;
    top: 44px; left: 0; width: 100%;
    text-align: center;
    font-size: 40px;
    font-weight: 400;
    color: var(--wine);
    letter-spacing: 1px;
    z-index: 2;
  }
  .series-rule {
    position: absolute;
    top: 100px; left: 143px;
    width: 572px; height: 1px;
    background: var(--rule);
    z-index: 2;
  }
  .series-title {
    position: absolute;
    top: 116px; left: 0; width: 100%;
    text-align: center;
    font-size: 100px;
    line-height: 100px;
    font-weight: 400;
    color: var(--paper);
    -webkit-text-stroke: 1.4px var(--outline);
    paint-order: stroke fill;
    letter-spacing: 1px;
    z-index: 2;
  }
  .instrument-line {
    position: absolute;
    top: 332px; left: 0; width: 100%;
    text-align: center;
    font-size: 44px;
    font-weight: 700;
    color: var(--wine);
    text-shadow: 0 0 6px var(--paper), 0 0 10px var(--paper);
    z-index: 3;
  }
  .hero-visual {
    position: absolute;
    top: 280px; left: 70px;
    width: 778px; height: 820px;
    background:
      linear-gradient(225deg,
        var(--sheet-light) 0%,
        var(--sheet-grey) 22%,
        var(--wood-light) 44%,
        var(--wood-mid) 62%,
        var(--wood-deep) 84%,
        var(--sheet-grey) 100%);
    -webkit-mask-image: radial-gradient(ellipse 52% 50% at 52% 52%, #000 58%, rgba(0,0,0,0) 100%);
    mask-image: radial-gradient(ellipse 52% 50% at 52% 52%, #000 58%, rgba(0,0,0,0) 100%);
    z-index: 1;
  }
  .work-credits {
    position: absolute;
    top: 922px; left: 250px; width: 420px;
    text-align: center;
    z-index: 3;
  }
  .composer, .work-title, .work-range {
    text-shadow:
      0 0 2px var(--paper), 0 0 4px var(--paper),
      0 0 8px var(--paper), 0 0 14px var(--paper);
  }
  .composer { font-size: 31px; font-weight: 700; color: var(--ink); line-height: 40px; }
  .work-title { font-size: 27px; font-weight: 600; color: var(--forest); line-height: 40px; }
  .work-range { font-size: 25px; font-weight: 600; color: var(--forest); line-height: 38px; }
  .author {
    position: absolute;
    top: 1118px; left: 0; width: 100%;
    text-align: center;
    font-size: 38px;
    font-weight: 400;
    color: var(--wine);
    letter-spacing: 0.5px;
    z-index: 2;
  }
</style>
</head>
<body>
  <main class="cover">
    <div class="series-name">The Weekly Handful Series</div>
    <div class="series-rule"></div>
    <h1 class="series-title">ENSEMBLE<br>FRAGMENTS</h1>
    <div class="instrument-line">For Viola</div>
    <div class="hero-visual" role="img" aria-label="Photograph of a viola lying diagonally over fanned sheets of printed music"></div>
    <div class="work-credits">
      <div class="composer">Anselm Korvath</div>
      <div class="work-title">Lune Orvel</div>
      <div class="work-range">Op. 20, measures 1-62</div>
    </div>
    <div class="author">Dariel Vomanek&nbsp; D.M.A.</div>
  </main>
</body>
</html>
```